Building company with a modern and unique product looking for a business card to help us stand out

We currently have a logo but as our business has grown, we feel that our business card is not reflecting our modern and high quality product and help us stand out from the crowd. Our business is mainly in the construction of new homes using a unique method and materials that makes our homes fire proof, vermin and pest resistant and rated to the maximum cyclone category (category 5). We need a business card that helps us stand out as well as communicating professionalism, high quality and trustworthiness. I have attached our current logo with a black and white option, as well as our business card which is double sided. We would like to retain as much of the information that is currently on our business cards, but presented in a more sleek way. We do like our current colour palette ( white, black, yellow and grey) and have been looking primarily at business cards with a black background however we are open to other combinations of colour and layout as long as we stand out. Please feel free to tweak our logo to make it more suitable for a business card, we like the black option that we use but we have had trouble trying to get the white area to match the rest of the logo and blend effectively into a business card. Please do not hesitate to contact us with any questions as we really want this to be successful!

Target Market(s)

Large contracts including government and larger companies

Industry/Entity Type

Business

Contact Information for Business Card

We will be providing this business card to potential clients including key government ministers and large funding companies, our business card should show that we are professional and reliable.

Requirements
Must have
• It must be easy to read and pleasing to the eye, It must contain as much of the information on the current business card and unless something really stands out, we will most likely pick a design that has all of the information included. It must include our logo of course and have some colour included.
Nice to have
• We are looking for a high end business card and would like to see designs that reflect this. We like the gloss/matte contrast, plastic cards with opaque/coloured areas and unique features not seen on everyday paper business cards. It would be nice to see a few different colour combinations, we are open to new ideas so please feel free to take some artistic licence.
Should not have
• Must not be too busy, difficult to read or be distracting from the information conveyed. Other than this please feel free to add your own touches and make it unique!

```html
<!DOCTYPE html>
<html lang="en">
<head>
<meta charset="utf-8">
<title>Kestrel Building Co. – Business Card</title>
<link rel="stylesheet" href="https://fonts.googleapis.com/css2?family=Open+Sans:wght@400;600;700&display=swap">
<style>
  :root {
    --bg: #ece9e4;
    --card: #ffffff;
    --ink: #1a1a1a;
    --gold: #c9a227;
    --grey: #d6d6d6;
    --cream: #f3ecd9;
    --shadow: rgba(0, 0, 0, 0.18);
  }
  html, body {
    margin: 0;
    width: 1200px;
    height: 900px;
    overflow: hidden;
    background: var(--bg);
    font-family: "Open Sans", Arial, sans-serif;
    color: var(--ink);
  }
  .canvas {
    position: relative;
    width: 1200px;
    height: 900px;
  }
  .card {
    position: absolute;
    width: 540px;
    height: 330px;
    background: var(--card);
    box-shadow: 0 10px 28px var(--shadow);
    overflow: hidden;
  }
  .card--back { left: 60px; top: 130px; }
  .card--front { left: 600px; top: 440px; }

  .back-pattern {
    position: absolute;
    inset: 0;
    background: linear-gradient(135deg, #f4f4f4 0%, var(--cream) 45%, #efefef 100%);
    opacity: 0.7;
  }
  .wordmark {
    position: absolute;
    display: flex;
    align-items: center;
    gap: 10px;
    font-weight: 700;
    color: var(--ink);
    white-space: nowrap;
  }
  .wordmark__square {
    width: 14px;
    height: 14px;
    background: var(--gold);
  }
  .card--back .wordmark { right: 34px; bottom: 44px; font-size: 24px; }
  .card--front .wordmark { left: 34px; bottom: 50px; font-size: 30px; }

  .contact {
    position: absolute;
    left: 300px;
    top: 36px;
    font-size: 13px;
    line-height: 1.35;
  }
  .contact__name {
    color: var(--gold);
    font-weight: 700;
    font-size: 15px;
    margin: 0;
  }
  .contact__role {
    margin: 0 0 16px 10px;
    font-size: 12.5px;
  }
  .contact__abn {
    margin: 0 0 14px 26px;
    font-weight: 700;
    font-size: 13.5px;
  }
  .contact__abn span { color: var(--gold); }
  .contact__list {
    list-style: none;
    margin: 0 0 0 46px;
    padding: 0;
  }
  .contact__list li {
    display: flex;
    align-items: center;
    gap: 10px;
    margin-bottom: 3px;
  }
  .contact__list svg {
    width: 11px;
    height: 11px;
    fill: var(--gold);
    flex: none;
  }
</style>
</head>
<body>
<main class="canvas">

  <section class="card card--back" aria-label="Card back">
    <div class="back-pattern" role="img" aria-label="Faint repeating pattern of the company's roof symbol in light grey and cream"></div>
    <div class="wordmark"><span class="wordmark__square"></span>Kestrel Building Co.</div>
  </section>

  <section class="card card--front" aria-label="Card front">
    <div class="contact">
      <p class="contact__name">Callum Reeves</p>
      <p class="contact__role">Managing Director</p>
      <p class="contact__abn"><span>ABN:</span> 47 208 315 660</p>
      <ul class="contact__list">
        <li>
          <svg viewBox="0 0 12 12" aria-hidden="true"><path d="M2.4 0.8 4 2.6 3.2 4.1c.7 1.6 2 2.9 3.7 3.7l1.5-.8 1.8 1.6-.9 2C5 10.4 1.6 7 .7 2.3z"/></svg>
          0412 305 781
        </li>
        <li>
          <svg viewBox="0 0 12 12" aria-hidden="true"><path d="M4 1h4v2h3v8H1V3h3zM5 2v1h2V2zM2 6v1h8V6z"/></svg>
          (02) 63 410 559
        </li>
        <li>
          <svg viewBox="0 0 12 12" aria-hidden="true"><path d="M0 2h12v8H0zm1 1v.4l5 3.2 5-3.2V3z"/></svg>
          hello@kestrelbuild.com.au
        </li>
      </ul>
    </div>
    <div class="wordmark"><span class="wordmark__square"></span>Kestrel Building Co.</div>
  </section>

</main>
</body>
</html>
```